A5 Personal trainer profile for corbell vitality

I need a A5 Landscape profile designed for the company I work for. Company name is Corbell Vitality. The profile is for personal trainers to let people know:

1. Brief description of themselves
2. Qualifications

A picture will be required on the right hand side of the profile. Corbell Vitality colours are green and white.

The Corbell Vitality Logo in the boarder of the example included must remain. We are looking for a clinical and professional design.

Industry/Entity Type

Health

```html
<!DOCTYPE html>
<html lang="en">
<head>
<meta charset="utf-8">
<title>Daniel Okoro – Personal Trainer Profile</title>
<link rel="stylesheet" href="https://fonts.googleapis.com/css2?family=Open+Sans:wght@400;600;700;800&family=Open+Sans+Condensed:wght@700&display=swap">
<style>
  :root {
    --green-deep: #0b6a37;
    --green-mid: #15883f;
    --green-light: #8cc63f;
    --white: #ffffff;
    --grey-band: #cfd3d6;
    --backdrop: #eef1ef;
    --photo-top: #d9ecc2;
    --photo-bottom: #a4cf72;
  }
  * { margin: 0; padding: 0; box-sizing: border-box; }
  html, body { width: 900px; height: 1200px; overflow: hidden; }
  body {
    background: var(--backdrop);
    font-family: "Open Sans", Arial, sans-serif;
    position: relative;
  }
  .profile-card {
    position: absolute;
    left: 20px; top: 296px;
    width: 860px; height: 608px;
    background: var(--white);
    overflow: hidden;
    box-shadow: 0 2px 10px rgba(0,0,0,0.12);
  }
  .card-shapes { position: absolute; inset: 0; }
  .trainer-name {
    position: absolute;
    left: 300px; top: 8px;
    font-family: "Open Sans Condensed", "Open Sans", sans-serif;
    font-weight: 700;
    font-size: 64px;
    line-height: 1;
    letter-spacing: 1px;
    color: var(--green-deep);
  }
  .trainer-role {
    position: absolute;
    left: 430px; top: 70px;
    font-family: "Open Sans Condensed", "Open Sans", sans-serif;
    font-weight: 700;
    font-size: 30px;
    color: var(--green-light);
  }
  .section-title {
    font-weight: 800;
    font-size: 27px;
    color: var(--white);
    letter-spacing: -0.3px;
    margin-bottom: 6px;
  }
  .help-section { position: absolute; left: 30px; top: 138px; width: 400px; }
  .clients-section { position: absolute; left: 30px; top: 300px; width: 320px; }
  .qualifications-section { position: absolute; left: 370px; top: 418px; width: 460px; }
  .tick-list { list-style: none; }
  .tick-list li {
    position: relative;
    padding-left: 22px;
    font-size: 13px;
    line-height: 1.45;
    color: var(--white);
  }
  .tick-list li::before {
    content: "";
    position: absolute;
    left: 3px; top: 3px;
    width: 5px; height: 10px;
    border-right: 2.5px solid var(--green-light);
    border-bottom: 2.5px solid var(--green-light);
    transform: rotate(40deg);
  }
  .client-quote {
    font-size: 13px;
    line-height: 1.5;
    color: var(--white);
  }
  .brand-mark {
    position: absolute;
    left: 380px; top: 572px;
    display: flex; align-items: center; gap: 6px;
    font-weight: 700;
    font-size: 18px;
    color: var(--white);
  }
  .brand-mark .brand-dot {
    width: 16px; height: 16px; border-radius: 50%;
    background: var(--white);
  }
</style>
</head>
<body>
  <main class="profile-card">
    <svg class="card-shapes" width="860" height="608" viewBox="0 0 860 608" aria-hidden="false">
      <defs>
        <linearGradient id="photoTone" x1="0" y1="0" x2="0" y2="1">
          <stop offset="0" stop-color="var(--photo-top)"/>
          <stop offset="1" stop-color="var(--photo-bottom)"/>
        </linearGradient>
      </defs>
      <rect class="trainer-photo" role="img" aria-label="Portrait photo of the personal trainer in a light green polo shirt"
            x="560" y="110" width="300" height="300" fill="url(#photoTone)"/>
      <path class="accent-curve" fill="var(--green-light)"
            d="M0,104 C220,100 390,96 432,150 C478,230 500,360 620,378 C720,392 800,388 860,382 L860,400 C800,404 700,410 600,392 C470,372 450,240 410,170 C380,124 220,122 0,124 Z"/>
      <path class="green-panel" fill="var(--green-deep)"
            d="M0,118 C220,116 380,112 420,160 C470,240 480,370 610,394 C710,412 800,404 860,398 L860,608 L0,608 Z"/>
      <path class="grey-band" fill="var(--grey-band)" d="M0,578 L360,578 L360,608 L0,608 Z"/>
    </svg>

    <h1 class="trainer-name">DANIEL OKORO</h1>
    <p class="trainer-role">Personal Trainer</p>

    <section class="help-section">
      <h2 class="section-title">How I can help you?</h2>
      <ul class="tick-list">
        <li>Reduce body fat and increase body definition</li>
        <li>Increase stamina, improve agility and speed</li>
        <li>Increase strength and size</li>
        <li>Plyometric training and conditioning</li>
        <li>Flexibility and core strength</li>
      </ul>
    </section>

    <section class="clients-section">
      <h2 class="section-title">What my clients say bout me?</h2>
      <p class="client-quote">"With Daniel my training is always challenging and fun. I don't remember a session to be boring or repetitive. In short time I improved my core strength and flexibility. I can run 10k without stopping. It is amazing improvement." Laura Pemberton</p>
    </section>

    <section class="qualifications-section">
      <h2 class="section-title">Qualifications</h2>
      <ul class="tick-list">
        <li>Advanced Circuit Training</li>
        <li>Advanced Diploma in Personal Training - Level 3 REPS Registered</li>
        <li>Fitness Instructor - Level 2 REPS Registered</li>
        <li>Also qualified in - Suspension training, Studio Cycling,<br>Sports Nutrition, Weight Management</li>
      </ul>
    </section>

    <div class="brand-mark"><span class="brand-dot"></span>Corbell Vitality</div>
  </main>
</body>
</html>
```